Oil & Gas Service Brochure

We need to create a brochure that highlights the benefits of one of our services to oil and gas wells. We have a word document that includes a summary of the service and its problem solving benefits as well as some photos. The task will be to create a brochure using this information and our company logo and color schemes. Additionally, copy editing and proofing is preferred.

Target Market(s)

Oil & Gas Well Operators

```html
<!DOCTYPE html>
<html lang="en">
<head>
<meta charset="utf-8">
<title>Slick Bolt System Brochure</title>
<link rel="stylesheet" href="https://fonts.googleapis.com/css2?family=Arimo:wght@400;700&family=Exo+2:ital,wght@1,800&display=swap">
<style>
  :root {
    --navy: #14148c;
    --navy-deep: #0d0d6e;
    --teal: #5a9096;
    --panel: #ededed;
    --paper: #f6f6f6;
    --ink: #1a1a1a;
    --stage: #e4e4e4;
    --chart-blue: #2b4fa8;
    --chart-green: #1f9a3a;
  }
  * { box-sizing: border-box; margin: 0; padding: 0; }
  html, body { width: 1200px; height: 853px; overflow: hidden; }
  body {
    background: var(--stage);
    font-family: "Arimo", Arial, sans-serif;
    color: var(--ink);
    position: relative;
  }
  .spread { position: absolute; top: 166px; height: 520px; display: flex; box-shadow: 0 6px 18px rgba(0,0,0,.18); }
  .spread--inside { left: 20px; }
  .spread--outside { left: 728px; }
  .panel { position: relative; width: 226px; height: 520px; background: var(--paper); overflow: hidden; }
  .panel + .panel { border-left: 1px solid #d8d8d8; }
  .band { position: absolute; left: 0; width: 100%; display: block; }

  /* Inside panel 1 */
  .process { padding: 24px 16px 0 16px; font-size: 6.9px; line-height: 1.28; }
  .process h2 { font-size: 10px; font-weight: 700; line-height: 1.2; margin-bottom: 12px; width: 130px; }
  .process ol { list-style: none; margin-bottom: 10px; }
  .process p { margin-bottom: 10px; }

  /* Photos */
  .photo { position: absolute; display: block; }
  .photo--grate { background: linear-gradient(160deg, #8d8a85 0%, #5b5347 45%, #9c968c 100%); }
  .photo--sub { background: linear-gradient(150deg, #3d3c38 0%, #8f8c85 40%, #b7ad5a 60%, #6e6b64 100%); }
  .photo--floor { background: linear-gradient(170deg, #b3ada3 0%, #8e887c 100%); }
  .caption { position: absolute; font-size: 6.6px; line-height: 1.3; }

  /* Charts */
  .chart { position: absolute; left: 14px; width: 198px; background: #fff; border: 1px solid #dcdcdc; }
  .chart text { font-family: "Arimo", Arial, sans-serif; }

  /* Outside: About */
  .about { background: var(--panel); }
  .about h2 { position: absolute; top: 120px; left: 22px; font-size: 14px; font-weight: 400; }
  .about p { position: absolute; top: 162px; left: 22px; right: 18px; font-size: 9.2px; line-height: 1.36; text-align: justify; }

  /* Cover */
  .cover { background: #fff; }
  .brand { position: absolute; top: 34px; left: 0; width: 100%; display: flex; align-items: center; justify-content: center; gap: 8px; color: var(--navy); }
  .brand__dot { width: 22px; height: 22px; border-radius: 50%; background: var(--navy); flex: none; }
  .brand__text { font-size: 11px; font-weight: 700; line-height: 1.15; }
  .brand__text small { display: block; font-size: 5.5px; font-weight: 700; letter-spacing: .3px; }
  .cover__scene { position: absolute; top: 96px; left: 0; width: 226px; height: 424px;
    background: linear-gradient(180deg, #1e3f96 0%, #2b3d8a 40%, #3a3570 62%, #7a5236 82%, #3b2a22 100%); }
  .cover__title { position: absolute; top: 205px; left: 0; width: 100%; text-align: center;
    font-family: "Exo 2", "Arial Black", sans-serif; font-style: italic; font-weight: 800;
    font-size: 17px; line-height: 1.3; color: #fff; letter-spacing: .3px; }
</style>
</head>
<body>

<!-- Inside spread -->
<section class="spread spread--inside">
  <article class="panel">
    <svg class="band" style="bottom:0" width="226" height="90" viewBox="0 0 226 90"><polygon points="0,36 226,0 226,90 0,90" fill="var(--navy)"/></svg>
    <div class="process">
      <h2>A typical job would look something like this</h2>
      <ol>
        <li>1. MIRU Slickline, RIH and pull plunger noting tight spots</li>
        <li>2. RIH and pull BSSV-note depth of nipple so we can correlate to tubing tally and wellbore diagram</li>
        <li>3. RIH with “dummy run” (Spang Jars, Weight bars, Blind Box and Temperature Probe) drift through Profile Nipples to determine Perf Sub depth, establish bottom hole temperature and to locate fluid level.</li>
        <li>4. Once depths, fluid level and temperature have been confirmed and we know we are deep enough to get into the Perf Sub, RIHW Slick Bolt System® and either perforate new holes using a RTG (Retrievable Tubing Gun) or remove scale utilizing our Scale Burst®.</li>
        <li>5. Free flow well to determine if new or more communication has been established.</li>
        <li>6. RIHW broach to production nipple. Reset production tools and turn well back to the client</li>
      </ol>
      <p>This service can be done in a few hours if no unexpected well conditions are encountered. The main benefits are:</p>
      <ol>
        <li>1. For a small investment, we can provide information on if the well needs to be worked over or not. IE if we perform this service and nothing changes, you know you have wellbore issues-NOT production tubing issues.</li>
        <li>2. This service is “greener” than a traditional workover by producing far less emissions. There is no need to kill the well or to flair any gas.</li>
        <li>3. When the service is successful, the data has shown an increase of 100%-600% in production! For example, we have stimulated wells that were making 2-3BBL/day before we performed this service, and they are now producing 50-70BBL/day!</li>
        <li>4. This service is cost effective enough that in most cases, the “free” increased production will pay for this service in 24-48 hours of running the well for 24-48 hours.</li>
      </ol>
    </div>
  </article>

  <article class="panel">
    <svg class="band" style="top:0" width="226" height="50" viewBox="0 0 226 50"><polygon points="0,0 226,0 226,20 0,48" fill="var(--teal)"/></svg>
    <div class="photo photo--grate" role="img" aria-label="Long scaled perforated sub laid on a steel grate in a shop" style="top:30px;left:10px;width:132px;height:250px"></div>
    <div class="photo photo--sub" role="img" aria-label="Perforated sub resting on a stand after scale removal" style="top:30px;left:148px;width:78px;height:195px"></div>
    <p class="caption" style="top:232px;left:150px;width:76px">Perforated Sub after utilizing Scale Burst. ALL scale removed from the sub opening the original 56 holes.</p>
    <div class="photo photo--floor" role="img" aria-label="Shop floor with the sub before cleaning" style="top:300px;left:44px;width:120px;height:120px"></div>
    <p class="caption" style="top:440px;left:14px;width:196px">Images 1-3: Perforated sub pulled from a well that was scaled off, cleaned in a surface test to show results using our Scale Burst.</p>
  </article>

  <article class="panel">
    <svg class="band" style="top:0" width="226" height="50" viewBox="0 0 226 50"><polygon points="0,10 226,0 226,6 0,48" fill="var(--teal)"/></svg>
    <div class="photo photo--sub" role="img" aria-label="Perforated sub on a stand showing all holes reopened" style="top:52px;left:14px;width:198px;height:170px"></div>
    <p class="caption" style="top:230px;left:14px;width:198px">Perforated Sub after utilizing Scale Burst. ALL scale removed from the sub opening the original 56 holes.</p>

    <svg class="chart" style="top:282px" width="198" height="100" viewBox="0 0 198 100">
      <text x="99" y="11" text-anchor="middle" font-size="5.5" font-weight="700" fill="var(--chart-blue)">Scale Burst: Case Well #001 - Production BPD</text>
      <g stroke="#e2e2e2" stroke-width=".5">
        <line x1="14" y1="22" x2="190" y2="22"/><line x1="14" y1="34" x2="190" y2="34"/>
        <line x1="14" y1="46" x2="190" y2="46"/><line x1="14" y1="58" x2="190" y2="58"/>
        <line x1="14" y1="70" x2="190" y2="70"/>
      </g>
      <polyline fill="none" stroke="var(--chart-blue)" stroke-width="1" points="14,64 26,66 38,62 50,68 62,64 74,66 86,62 98,30 110,32 122,36 134,32 146,32 158,32 170,28 182,28 190,30"/>
      <g fill="var(--chart-blue)"><circle cx="98" cy="30" r="1"/><circle cx="134" cy="32" r="1"/><circle cx="170" cy="28" r="1"/></g>
      <text x="99" y="92" text-anchor="middle" font-size="4.5" font-weight="700" fill="var(--chart-blue)">Date - Scale Burst Performed 5/18/2022</text>
    </svg>

    <svg class="chart" style="top:392px" width="198" height="100" viewBox="0 0 198 100">
      <text x="99" y="10" text-anchor="middle" font-size="4.8" font-weight="700" fill="var(--chart-blue)">Daily Production Before / After Scale Burst Service - Case Well #001</text>
      <text x="99" y="17" text-anchor="middle" font-size="4.8" font-weight="700" fill="var(--chart-green)">427% Increase in Production</text>
      <g stroke="#e2e2e2" stroke-width=".5">
        <line x1="14" y1="26" x2="176" y2="26"/><line x1="14" y1="40" x2="176" y2="40"/>
        <line x1="14" y1="54" x2="176" y2="54"/><line x1="14" y1="68" x2="176" y2="68"/>
        <line x1="14" y1="82" x2="176" y2="82"/>
      </g>
      <polyline fill="none" stroke="var(--chart-blue)" stroke-width="1" points="40,80 130,32"/>
      <g fill="var(--chart-blue)"><circle cx="40" cy="80" r="1.3"/><circle cx="130" cy="32" r="1.3"/></g>
      <text x="40" y="93" text-anchor="middle" font-size="3.8" fill="#555">Average Daily Production - Before</text>
      <text x="140" y="93" text-anchor="middle" font-size="3.8" fill="#555">Average Daily Production - After</text>
    </svg>
  </article>
</section>

<!-- Outside spread -->
<section class="spread spread--outside">
  <article class="panel about">
    <svg class="band" style="top:0" width="226" height="100" viewBox="0 0 226 100"><polygon points="0,0 226,0 226,94 0,82" fill="var(--navy)"/></svg>
    <h2>About Us</h2>
    <p>The origin of this service started in the DJ Basin when we discovered a need to increase production on older producing Plunger Lift wells. We found that after multiple rig workovers, the issue was not in the wellbore itself, but that the Perf or Slotted Sub had become either scaled or sanded off choking the well down to very little or no flow. Realizing the issue was fixable without doing an expensive traditional Workover, we purchased a device that allows us to perform basic ballistic procedures safely off our Slickline units. There are no other standard mechanical or hydraulic slickline perforating tools that can accomplish this service available.</p>
    <svg class="band" style="bottom:0" width="226" height="100" viewBox="0 0 226 100"><polygon points="0,4 226,0 226,100 0,100" fill="var(--navy)"/></svg>
  </article>

  <article class="panel cover">
    <div class="brand">
      <span class="brand__dot"></span>
      <span class="brand__text">Crestline Directional Solutions<small>A CRESTLINE OILFIELD SERVICES COMPANY</small></span>
    </div>
    <div class="cover__scene" role="img" aria-label="Refinery towers lit at dusk against a blue sky"></div>
    <svg class="band" style="top:96px" width="226" height="424" viewBox="0 0 226 424">
      <polygon points="226,0 226,18 0,120 0,112" fill="var(--teal)"/>
      <polygon points="226,20 226,26 8,122" fill="var(--teal)" opacity=".75"/>
      <polygon points="226,20 226,300 20,300 8,122" fill="var(--navy)" opacity=".35"/>
      <polygon points="0,300 226,352 226,372 0,310" fill="var(--teal)"/>
    </svg>
    <h1 class="cover__title">SLICK BOLT<br>SYSTEM<br>FOR WELL<br>STIMULATION<br>AND<br>SCALE REMOVAL<br>SERVICES</h1>
  </article>
</section>

</body>
</html>
```